Home page and features page design for SaaS company

We're looking for designs for a home page and a features page of a new website (possibly more pages to be commissioned thereafter). The website is called 'Plainly Afloat' and is a service that helps swimming clubs and schools reduce administration.

The website will have a clean, minimalist, modern feel but not corporate. Here's an idea of the type of style: https://rostrik.net/pages/payments

At the top of the home page (above the fold) will show the two personas that the website is targeting (Swimming clubs and Swimming Schools) on a styled background (no cheesy stock images please!). Those personas can be represented as an illustration (see page 2 for an example), line art graphic or icon and will link through to a features page.

For your information, the type of people that are members of swimming clubs include beginners, competitive squads and adult swimmers. People that attend a swimming school are typically children learning to swim. If you can represent the above in simple line art illustrations/graphics/icons that match the style of our logo - great!

Below the fold on the home page will be an illustration of the main functions of the site (with our logo central to that) and at the bottom of the page will be what they get for free, testimonials and a call to action for booking a demo.

I've attached a simple wireframe of the home page for your information.

The second page is the features page. This summarises the benefits of each major feature. Each feature listed on the page is separated by a call to action. Here's a link to the content of the features page: http://webnode4.quillar-advisory.com/KTRmarketingpages/swimming/swim-club-management-software.html

Don't take a lead from the look / feel / design of this page. I don't like it (hence I'm on here to find a better design!). One thing I'd like to incorporate is a snippet preview of a screenshot on the features page (a bit like in the example). The user can click on this and the full screenshot will load in a pop-up.

The style of the features page should flow from the home page.
Updates

Project Deadline Extended
Reason: Extending deadline to allow more quality designs and give those that have submitted time to make any revisions.

Target Market(s)

Swimming clubs and swimming schools

Industry/Entity Type

Internet

Number of Pages Required

2 page

Font styles to use
Sans Serif

Colors
33a6d7
33b8a4

Requirements
Must have
• Clean, minimalist, modern feel but not corporate. Here's an idea of the type of style: https://rostrik.net/pages/payments
Should not have
• Unstylised stock photographs

```html
<!DOCTYPE html>
<html lang="en">
<head>
<meta charset="utf-8">
<title>Plainly Afloat – Membership software for swimming clubs and schools</title>
<link rel="stylesheet" href="https://fonts.googleapis.com/css2?family=Roboto:wght@300;400;500;700&display=swap">
<style>
  :root {
    --hero-dark: #1e2748;
    --hero-mid: #2f4a86;
    --hero-light: #5f9fd8;
    --brand-blue: #4aa7dc;
    --accent-blue: #1b84c8;
    --nav-button: #1a9ad6;
    --ink: #1d1d1d;
    --body-ink: #555555;
    --muted-ink: #777777;
    --panel-grey: #efefef;
    --ring-grey: #e6e6e6;
    --footer-bg: #3b3b3b;
    --footer-rule: #4c4c4c;
    --dot-active: #f0a500;
    --dot-idle: #3d4049;
    --white: #ffffff;
  }
  * { box-sizing: border-box; margin: 0; padding: 0; }
  html, body { width: 1200px; height: 2305px; overflow: hidden; }
  body { font-family: "Roboto", Arial, sans-serif; color: var(--ink); background: var(--white); position: relative; }
  a { color: inherit; text-decoration: none; }

  /* Hero */
  .hero {
    position: absolute; left: 0; top: 0; width: 1200px; height: 570px;
    background: linear-gradient(100deg, var(--hero-dark) 0%, var(--hero-mid) 50%, var(--hero-light) 100%);
    color: var(--white);
  }
  .brand { position: absolute; left: 88px; top: 20px; display: flex; align-items: center; gap: 14px; }
  .brand-dot { width: 30px; height: 30px; border-radius: 50%; background: var(--brand-blue); }
  .brand-name { font-size: 26px; font-weight: 400; color: var(--white); }
  .main-nav { position: absolute; right: 88px; top: 28px; display: flex; align-items: center; gap: 24px; font-size: 14px; }
  .main-nav .nav-cta { background: var(--nav-button); padding: 7px 9px; }
  .hero-title { position: absolute; top: 118px; width: 100%; text-align: center; font-size: 31px; font-weight: 300; }
  .persona-card {
    position: absolute; top: 212px; width: 270px; height: 270px; background: var(--brand-blue);
    padding: 97px 0 0 20px;
  }
  .persona-card.clubs { left: 189px; }
  .persona-card.schools { left: 762px; padding-left: 32px; }
  .persona-title { font-size: 25px; font-weight: 700; margin-bottom: 7px; }
  .persona-button {
    display: inline-block; background: #262626; border: 1px solid #dcdcdc;
    font-size: 16px; padding: 7px 18px; color: var(--white);
  }
  .persona-figure {
    position: absolute; border-radius: 60px 60px 20px 20px;
    background: linear-gradient(180deg, #4c86c4 0%, #f1f1f1 45%, #3f86c4 100%); opacity: .9;
  }
  .persona-figure.coach { left: 418px; top: 240px; width: 126px; height: 324px; }
  .persona-figure.teacher { left: 656px; top: 252px; width: 112px; height: 310px; }

  /* Features wheel */
  .features { position: absolute; left: 0; top: 570px; width: 1200px; height: 618px; }
  .hub-ring { position: absolute; left: 507px; top: 224px; width: 178px; height: 178px; border-radius: 50%; border: 2px solid #eeeeee; }
  .hub-core {
    position: absolute; left: 524px; top: 241px; width: 144px; height: 144px; border-radius: 50%;
    background: var(--ring-grey); display: flex; align-items: center; justify-content: center;
    font-size: 18px; font-weight: 500; color: var(--accent-blue); text-align: center;
  }
  .feature-icon {
    position: absolute; width: 80px; height: 80px; border-radius: 50%; border: 2px solid #3a3a3a;
    background: var(--white); display: flex; align-items: center; justify-content: center;
  }
  .feature-icon svg { width: 38px; height: 38px; }
  .feature-label { position: absolute; font-size: 20px; font-weight: 500; white-space: nowrap; }
  .feature-label.right-aligned { text-align: right; }

  /* Benefits grid */
  .benefits { position: absolute; left: 0; top: 1188px; width: 1200px; height: 407px; background: var(--panel-grey); }
  .benefit-grid { position: absolute; left: 138px; top: 57px; width: 908px; display: grid; grid-template-columns: repeat(4, 227px); grid-auto-rows: 145px; }
  .benefit-text { background: var(--white); text-align: center; padding: 22px 16px 0; }
  .benefit-title { font-size: 12px; font-weight: 700; color: var(--accent-blue); margin-bottom: 10px; letter-spacing: .2px; }
  .benefit-body { font-size: 13px; line-height: 18px; color: var(--body-ink); margin-bottom: 9px; }
  .read-more { font-size: 11px; color: var(--accent-blue); }
  .benefit-photo { background: linear-gradient(135deg, #7a6a5c 0%, #b9c3cc 50%, #3e4e60 100%); }
  .benefit-photo.screen { background: linear-gradient(135deg, #31506e 0%, #d6dde4 60%, #587791 100%); }
  .benefit-photo.teamwork { background: linear-gradient(135deg, #1c2e4c 0%, #c08a52 50%, #3d77a8 100%); }

  /* Testimonials */
  .testimonials { position: absolute; left: 0; top: 1595px; width: 1200px; height: 449px; }
  .section-title { position: absolute; top: 39px; width: 100%; text-align: center; font-size: 25px; font-weight: 400; }
  .section-rule { position: absolute; left: 545px; top: 74px; width: 77px; height: 2px; background: #333; }
  .quote-card {
    position: absolute; top: 110px; height: 246px; background: var(--white);
    box-shadow: 0 0 0 1px #ececec, 4px 5px 0 0 #f2f2f2; padding: 20px 32px 0;
  }
  .quote-card.first { left: 155px; width: 423px; }
  .quote-card.second { left: 625px; width: 429px; }
  .quote-mark { font-size: 40px; font-weight: 700; color: var(--brand-blue); line-height: 30px; height: 34px; }
  .quote-text { font-size: 12.5px; line-height: 20.5px; color: var(--body-ink); }
  .quote-author { display: flex; align-items: center; gap: 14px; margin-top: 20px; }
  .author-photo { width: 52px; height: 52px; border-radius: 50%; background: linear-gradient(160deg, #d9c2ae, #8d7766); }
  .author-name { font-size: 13px; font-weight: 500; color: var(--ink); }
  .author-role { font-size: 12px; color: var(--muted-ink); margin-top: 4px; }
  .slider-dots { position: absolute; top: 390px; left: 584px; display: flex; gap: 6px; }
  .slider-dots span { width: 11px; height: 11px; border-radius: 50%; background: var(--dot-idle); }
  .slider-dots span.active { background: var(--dot-active); }

  /* Footer */
  .site-footer { position: absolute; left: 0; top: 2044px; width: 1200px; height: 261px; background: var(--footer-bg); color: var(--white); text-align: center; }
  .demo-title { position: absolute; top: 34px; width: 100%; font-size: 41px; font-weight: 300; }
  .demo-button { position: absolute; left: 475px; top: 92px; width: 220px; height: 43px; background: var(--brand-blue); font-size: 16px; line-height: 43px; }
  .footer-rule { position: absolute; left: 146px; top: 164px; width: 908px; height: 1px; background: var(--footer-rule); }
  .footer-nav { position: absolute; top: 181px; width: 100%; display: flex; justify-content: center; gap: 22px; font-size: 14px; }
  .copyright { position: absolute; top: 218px; width: 100%; font-size: 11px; font-weight: 500; }
</style>
</head>
<body>

<header class="hero">
  <a class="brand" href="#"><span class="brand-dot"></span><span class="brand-name">Plainly Afloat</span></a>
  <nav class="main-nav">
    <a href="#">About us</a><a href="#">Pricing</a><a href="#">Free resources</a><a href="#">Free account</a><a class="nav-cta" href="#">Contact us</a>
  </nav>
  <h1 class="hero-title">Membership software for swimming clubs and schools</h1>

  <div class="persona-card clubs">
    <h2 class="persona-title">Swimming Clubs</h2>
    <a class="persona-button" href="#">Find out more</a>
  </div>
  <div class="persona-figure coach" role="img" aria-label="Illustration of a swimming club coach with cap and whistle"></div>

  <div class="persona-figure teacher" role="img" aria-label="Illustration of a swimming school teacher holding a tablet"></div>
  <div class="persona-card schools">
    <h2 class="persona-title">Swimming Schools</h2>
    <a class="persona-button" href="#">Find out more</a>
  </div>
</header>

<section class="features">
  <div class="hub-ring"></div>
  <div class="hub-core">Plainly<br>Afloat</div>

  <span class="feature-label" style="left:0;width:1192px;text-align:center;top:61px;">Online payments</span>
  <div class="feature-icon" style="left:559px;top:103px;">
    <svg viewBox="0 0 40 40"><path d="M14 9h12l-3 5c6 3 9 9 9 15 0 4-4 6-12 6S8 33 8 29c0-6 3-12 9-15z" fill="#111"/><text x="20" y="30" font-size="12" font-family="Arial" font-weight="700" fill="#fff" text-anchor="middle">$</text></svg>
  </div>

  <span class="feature-label right-aligned" style="right:808px;top:181px;">Online registrations</span>
  <div class="feature-icon" style="left:413px;top:166px;">
    <svg viewBox="0 0 40 40" fill="none" stroke="#111" stroke-width="2.4"><rect x="6" y="7" width="28" height="24"/><line x1="6" y1="13" x2="34" y2="13"/><line x1="11" y1="19" x2="29" y2="19"/><line x1="11" y1="25" x2="22" y2="25"/><path d="M25 27l4 6 3-3" /></svg>
  </div>

  <span class="feature-label" style="left:796px;top:181px;">Financial reporting</span>
  <div class="feature-icon" style="left:694px;top:157px;">
    <svg viewBox="0 0 40 40" fill="none" stroke="#111" stroke-width="2.4"><path d="M10 5h16l6 6v24H10z"/><line x1="15" y1="22" x2="27" y2="22"/><line x1="15" y1="27" x2="27" y2="27"/><circle cx="22" cy="14" r="3"/><circle cx="10" cy="32" r="5" fill="#111"/></svg>
  </div>

  <span class="feature-label right-aligned" style="right:836px;top:314px;">Attendance register</span>
  <div class="feature-icon" style="left:381px;top:290px;">
    <svg viewBox="0 0 40 40" fill="none" stroke="#111" stroke-width="2.4"><rect x="8" y="6" width="22" height="28"/><line x1="12" y1="13" x2="24" y2="13"/><line x1="12" y1="19" x2="24" y2="19"/><line x1="12" y1="25" x2="20" y2="25"/><path d="M34 12L22 30l-3 2 1-4 12-17z" fill="#111"/></svg>
  </div>

  <span class="feature-label" style="left:830px;top:307px;">Membership data</span>
  <div class="feature-icon" style="left:728px;top:277px;">
    <svg viewBox="0 0 40 40"><ellipse cx="18" cy="9" rx="11" ry="4" fill="#1b84c8"/><path d="M7 12c0 3 22 3 22 0v6c0 3-22 3-22 0zM7 21c0 3 22 3 22 0v6c0 3-22 3-22 0z" fill="#1b84c8"/><circle cx="29" cy="28" r="5" fill="none" stroke="#111" stroke-width="2.4"/><line x1="32" y1="32" x2="36" y2="36" stroke="#111" stroke-width="2.4"/></svg>
  </div>

  <span class="feature-label right-aligned" style="right:787px;top:448px;">Event management</span>
  <div class="feature-icon" style="left:433px;top:413px;">
    <svg viewBox="0 0 40 40" fill="none" stroke="#111" stroke-width="2.4"><rect x="5" y="8" width="24" height="22"/><line x1="5" y1="14" x2="29" y2="14"/><line x1="11" y1="5" x2="11" y2="10"/><line x1="23" y1="5" x2="23" y2="10"/><circle cx="29" cy="29" r="7" fill="#fff"/><path d="M29 25v4h3"/></svg>
  </div>

  <span class="feature-label" style="left:793px;top:420px;">Group email</span>
  <div class="feature-icon" style="left:693px;top:384px;">
    <svg viewBox="0 0 40 40"><text x="20" y="14" font-size="13" font-family="Arial" font-weight="700" text-anchor="middle" fill="#111">@</text><circle cx="12" cy="22" r="3.5" fill="#111"/><circle cx="28" cy="22" r="3.5" fill="#111"/><circle cx="20" cy="21" r="4" fill="#111"/><path d="M5 35c0-6 4-9 7-9s5 2 5 4M35 35c0-6-4-9-7-9s-5 2-5 4M12 35c0-6 4-9 8-9s8 3 8 9z" fill="#111"/></svg>
  </div>

  <span class="feature-label" style="left:0;width:1202px;text-align:center;top:548px;">Galas</span>
  <div class="feature-icon" style="left:562px;top:453px;">
    <svg viewBox="0 0 40 40" fill="none" stroke="#111" stroke-width="2.4"><path d="M8 12h10l-1 8c-1 3-7 3-8 0z"/><line x1="13" y1="23" x2="13" y2="32"/><line x1="9" y1="32" x2="17" y2="32"/><path d="M22 12h10l-1 8c-1 3-7 3-8 0z"/><line x1="27" y1="23" x2="27" y2="32"/><line x1="23" y1="32" x2="31" y2="32"/></svg>
  </div>
</section>

<section class="benefits">
  <div class="benefit-grid">
    <div class="benefit-photo" role="img" aria-label="Photo of hands on a laptop showing the software dashboard"></div>
    <div class="benefit-text">
      <h3 class="benefit-title">SOFTWARE UPDATES</h3>
      <p class="benefit-body">Pellentesque fringilla fringilla sapien, sit amet porttitor purus tempus purus.</p>
      <a class="read-more" href="#">READ MORE &#9656;</a>
    </div>
    <div class="benefit-photo" role="img" aria-label="Photo of a laptop showing a sign-in form"></div>
    <div class="benefit-text">
      <h3 class="benefit-title">FIRST CLASS SUPPORT</h3>
      <p class="benefit-body">Pellentesque fringilla fringilla sapien, sit amet porttitor purus tempus purus.</p>
      <a class="read-more" href="#">READ MORE &#9656;</a>
    </div>
    <div class="benefit-text">
      <h3 class="benefit-title">ACCESS TO EXCLUSIVE TOOLS</h3>
      <p class="benefit-body">Pellentesque fringilla fringilla sapien, sit amet porttitor purus tempus purus.</p>
      <a class="read-more" href="#">READ MORE &#9656;</a>
    </div>
    <div class="benefit-photo screen" role="img" aria-label="Photo of a laptop screen showing a software update"></div>
    <div class="benefit-text">
      <h3 class="benefit-title">ACCOUNT SETUP</h3>
      <p class="benefit-body">Pellentesque fringilla fringilla sapien, sit amet porttitor purus tempus purus.</p>
      <a class="read-more" href="#">READ MORE &#9656;</a>
    </div>
    <div class="benefit-photo teamwork" role="img" aria-label="Photo of hands joining coloured puzzle pieces"></div>
  </div>
</section>

<section class="testimonials">
  <h2 class="section-title">Our Clients Say</h2>
  <div class="section-rule"></div>

  <article class="quote-card first">
    <div class="quote-mark">&ldquo;</div>
    <p class="quote-text">Nulla sodales mauris lorem, vitae dapibus nibh varius a. Etiam urna mauris, ultricies quis nulla nec, tempor interdum metus. Donec vel mattis augue. Quisque justo dolor, lobortis non metus fermentum, dignissim sollicitudin nulla. Nulla sodales purus tortor, eu scelerisque arcu pharetra aliquam.</p>
    <div class="quote-author">
      <div class="author-photo" role="img" aria-label="Portrait of the client"></div>
      <div><div class="author-name">Dariel Monrow</div><div class="author-role">manager</div></div>
    </div>
  </article>

  <article class="quote-card second">
    <div class="quote-mark">&ldquo;</div>
    <p class="quote-text">Nulla sodales mauris lorem, vitae dapibus nibh varius a. Etiam urna mauris, ultricies quis nulla nec, tempor interdum metus. Donec vel mattis augue. Quisque justo dolor, lobortis non metus fermentum, dignissim sollicitudin nulla. Nulla sodales purus tortor, eu scelerisque arcu pharetra aliquam.</p>
    <div class="quote-author">
      <div class="author-photo" role="img" aria-label="Portrait of the client"></div>
      <div><div class="author-name">Tobin Hale</div><div class="author-role">manager</div></div>
    </div>
  </article>

  <div class="slider-dots"><span class="active"></span><span></span><span></span></div>
</section>

<footer class="site-footer">
  <h2 class="demo-title">Book a free demo now</h2>
  <a class="demo-button" href="#">Click Here</a>
  <div class="footer-rule"></div>
  <nav class="footer-nav">
    <a href="#">About us</a><a href="#">Pricing</a><a href="#">Free resources</a><a href="#">Free account</a><a href="#">Contact us</a>
  </nav>
  <p class="copyright">&copy; 2017. Plainly Afloat All Rights Reserved.</p>
</footer>

</body>
</html>
```